Name of Business: KORL Advisory. It is a consulting and advisory business providing Investment and f

I am looking for a letterhead (preferably in word) design for a new business that portarys the attributes of professionalism, honesty, integrity and impartiality. I operate in a Regional area called Ocean Grove which is located about 90min drive from Melbourne CBD on the Victorian coast.

I have an open mind on design and colour: like all things creative it will either hit the spot or not.
Updates

Hi - Thank you all for your disigns. We are currently travelling in Australia and can't always get an internet coonnections. We are reviewing all designs and will try and get back to each of your over the next few days. Derek Plimsey

Industry/Entity Type

Business

```html
<!DOCTYPE html>
<html lang="en">
<head>
<meta charset="utf-8">
<title>KORL Advisory – Stationery</title>
<link rel="stylesheet" href="https://fonts.googleapis.com/css2?family=Carlito:ital,wght@0,400;0,700&family=Raleway:wght@300;400;500;600&display=swap">
<style>
  :root {
    --brand-red: #b3473d;
    --paper: #f7f7f7;
    --backdrop: #e9e9e9;
    --ink: #2b2b2b;
    --white: #ffffff;
    --signature-tone: rgba(43,43,43,.10);
  }
  * { box-sizing: border-box; margin: 0; padding: 0; }
  html, body { width: 1200px; height: 1000px; overflow: hidden; }
  body { background: var(--backdrop); position: relative; font-family: "Carlito", "Calibri", sans-serif; color: var(--ink); }

  .letterhead { position: absolute; left: 123px; top: 77px; width: 602px; height: 850px; background: var(--paper); box-shadow: 0 2px 12px rgba(0,0,0,.12); }

  .wordmark { position: absolute; display: flex; align-items: center; gap: 6px; font-family: "Carlito", "Calibri", sans-serif; font-weight: 700; white-space: nowrap; line-height: 1; }
  .wordmark__square { width: 10px; height: 10px; background: currentColor; flex: none; }
  .letterhead .wordmark { left: 30px; top: 41px; color: var(--brand-red); font-size: 17px; }

  .header-band { position: absolute; left: 160px; top: 19px; width: 442px; height: 61px; background: var(--brand-red); color: var(--white); font-family: "Raleway", sans-serif; font-weight: 300; font-size: 18px; display: flex; align-items: center; justify-content: center; }

  .subject { position: absolute; left: 192px; top: 181px; width: 272px; font-size: 11.8px; line-height: 14.5px; }
  .subject strong { display: block; }

  .meta { position: absolute; left: 40px; width: 126px; text-align: right; font-size: 11.8px; line-height: 14.5px; }
  .meta dt { font-weight: 700; }
  .meta--date { top: 259px; }
  .meta--from { top: 321px; }
  .meta--to { top: 411px; }

  .body-copy { position: absolute; left: 182px; top: 259px; width: 358px; font-size: 11.8px; line-height: 14.6px; text-align: justify; hyphens: auto; }
  .body-copy p { text-indent: 10px; }
  .body-copy p.gap { margin-top: 14px; }

  .signature { position: absolute; left: 169px; top: 706px; width: 88px; height: 22px; background: linear-gradient(90deg, var(--signature-tone), rgba(43,43,43,.03)); border-radius: 11px; }
  .signature-name { position: absolute; left: 190px; top: 730px; font-size: 7px; letter-spacing: .3px; }

  .footer-band { position: absolute; left: 0; bottom: 0; width: 602px; height: 41px; background: var(--brand-red); color: var(--white); font-size: 11.5px; display: flex; align-items: center; justify-content: center; white-space: nowrap; }
  .footer-band b { font-weight: 700; margin-right: 3px; }

  .card { position: absolute; width: 260px; height: 144px; box-shadow: 0 2px 10px rgba(0,0,0,.14); }
  .card--front { left: 820px; top: 512px; background: var(--brand-red); }
  .card--front .wordmark { left: 0; right: 0; top: 62px; justify-content: center; color: var(--white); font-size: 22px; }
  .card--front .wordmark__square { width: 13px; height: 13px; }
  .card--back { left: 817px; top: 733px; background: var(--white); }
  .card__tagline { position: absolute; left: 0; right: 0; top: 44px; text-align: center; color: var(--brand-red); font-family: "Raleway", sans-serif; font-size: 16px; line-height: 17px; }
  .card__tagline span { display: block; }
  .card__tagline .light { font-weight: 300; }
  .card__tagline .regular { font-weight: 400; }
  .card__tagline .medium { font-weight: 500; }
  .card__contact { position: absolute; left: 0; right: 0; bottom: 16px; text-align: center; font-size: 5px; color: var(--ink); white-space: nowrap; }
  .card__contact b { font-weight: 700; }
</style>
</head>
<body>
  <article class="letterhead">
    <div class="wordmark"><span class="wordmark__square"></span>KORL Advisory</div>
    <div class="header-band">Consulting and Advisory Business</div>

    <div class="subject">
      <strong>Lorem ipsum dolor sit amet, ei eros vidit sonet eum</strong>
      Te vidisse recteque pro, cu per habemus officiis, eos ex malis posidonium omittantur.
    </div>

    <dl class="meta meta--date"><dt>Date</dt><dd>September 25, 2014</dd></dl>
    <dl class="meta meta--from"><dt>From</dt><dd>Mr. Owen Marsh<br>Financial Director<br>Investments</dd></dl>
    <dl class="meta meta--to"><dt>To</dt><dd>Mr. Liam Carver<br>CEO Business Solution</dd></dl>

    <div class="body-copy">
      <p>Lorem ipsum dolor sit amet, ei eros vidit sonet eum, sed ea aliquam offendit. Reque quando labitur nec in, no solum ceteros est. Accumsan pertinacia an qui. Te vidisse recteque pro, cu per habemus officiis, eos ex malis posidonium omittantur.</p>
      <p>Lorem ipsum dolor sit amet, ei eros vidit sonet eum, sed ea aliquam offendit. Reque quando labitur nec in, no solum ceteros est. Accumsan pertinacia an qui. Te vidisse recteque pro, cu per habemus officiis, eos ex malis posidonium omittantur. Appetere principes eloquentiam vis ei, an mea alia petentium dignissim, te justo omnium duo.</p>
      <p class="gap">Movet laoreet delicatissimi cum id. Essent dissentiet cu cum, atqui augue iriure qui ea. Liber propriae ei sed. Euismod ornatus scaevola et pro.</p>
      <p class="gap">Verterem interesset disputationi vim et, laudem persecuti quo eu. Mea viderer vulputate ut. Ad scripta scaevola appetere usu, omnium forensibus sed cu, dolorum admodum postulant mea ei. Eos ut ubique graeco insolens, etiam electram assentior cum at.</p>
      <p class="gap">In eos solum verterem facilisis, magna scaevola explicari has ex, at vidisse percipitur cum. At dicam postea luptatum sea, sed te timeam principes disputando, postea scaevola eloquentiam quo eu. Cetero concludaturque cu ius, nam erat detraxit ut, in his cetero vocent erroribus. Eu sint nulla comprehensam qui. Dolor dolorum splendide ei est, id usu inani liber deterruisset.</p>
    </div>

    <div class="signature" role="img" aria-label="Handwritten signature"></div>
    <div class="signature-name">NAME / C.E.O</div>

    <footer class="footer-band"><b>PHONE</b> 000 000 000 /&nbsp;<b>FAX</b> 000000 0000 / 12 Shore Rd, Ocean Grove / hello@korladvisory.com.au</footer>
  </article>

  <section class="card card--front">
    <div class="wordmark"><span class="wordmark__square"></span>KORL Advisory</div>
  </section>

  <section class="card card--back">
    <div class="card__tagline"><span class="light">CONSULTING</span><span class="regular">ADVISORY</span><span class="medium">BUSINESS</span></div>
    <div class="card__contact"><b>PHONE:</b> 000 000 000 / <b>FAX:</b> 000000 0000 / <b>STREET:</b> 12 Shore Rd, Ocean Grove / <b>EMAIL:</b> hello@korladvisory.com.au</div>
  </section>
</body>
</html>
```